Webshop Template

For our Webstore in UK we need a complete Template,
shoppingcart is Magento, the Shop is focussed on Download software,

the name: Appvaultdepot.co.uk

Check out some other good stores, like lumawerk.de

for example the Page from 

www.brenvik.co.uk or

www.lumawerk.de

www.tastenhugo.de

www.klickrabatt.de

The Logodesign which are in Consideration

http://www.artmosaiq.com/design/5520817/logo-design-by-tomasz7kv

http://www.artmosaiq.com/design/5518360/logo-design-by-luisgaviota

http://www.artmosaiq.com/design/5517245/logo-design-by-kestrel-works

http://www.artmosaiq.com/design/5516093/logo-design-by-zumbiloft

http://www.artmosaiq.com/design/5515471/logo-design-by-tivaro

http://www.artmosaiq.com/design/5514902/logo-design-by-blue-fern-graphics-

Target Market(s)

B2C - Consumer Marcet

Industry/Entity Type

Shop

```html
<!DOCTYPE html>
<html lang="en">
<head>
<meta charset="utf-8">
<title>Appvaultdepot.co.uk – Webshop Template</title>
<link href="https://fonts.googleapis.com/css2?family=PT+Sans:wght@400;700&display=swap" rel="stylesheet">
<style>
:root{
  --dark:#2a2b2d;
  --red:#d8443f;
  --red-soft:#e0645f;
  --red-text:#c9302c;
  --page:#ededed;
  --slider:#c3c3c3;
  --muted:#888;
  --line:#9a9a9a;
  --white:#fff;
  --footer-text:#e6e6e6;
}
*{margin:0;padding:0;box-sizing:border-box}
html,body{width:1200px;height:1187px;overflow:hidden}
body{position:relative;background:var(--page);font-family:Arial,Helvetica,sans-serif;color:#555}
.abs{position:absolute}
ul{list-style:none}

.topbar{left:0;top:0;width:1200px;height:24px;background:var(--dark);border-bottom:3px solid var(--red);font-size:10px;color:#ccc}
.topbar .currency{left:233px;top:6px}
.topbar .currency b{color:var(--red-soft);font-weight:400}
.topbar .links{right:227px;top:6px}
.topbar .links .welcome{color:var(--red-soft);font-weight:700;margin-right:6px}
.topbar .links span.sep{margin:0 4px;color:#888}

.logo{left:235px;top:60px;font-family:"PT Sans",sans-serif;font-size:29px;font-weight:700;color:#b3141b;letter-spacing:.5px}
.tel{left:482px;top:43px;font-size:10px;color:#999}
.search{left:482px;top:63px;display:flex}
.search .field{width:144px;height:18px;background:var(--white);border:1px solid #ddd;font-size:9px;color:#aaa;padding:3px 10px}
.search .btn{width:40px;height:18px;background:var(--red);color:var(--white);font-size:8px;font-weight:700;text-align:center;line-height:18px}
.cart{right:227px;top:43px;font-size:10px;color:#777;display:flex;align-items:center;gap:4px}
.cart b{color:var(--red-text)}

.nav{left:0;top:125px;width:1200px;height:37px;background:linear-gradient(#d9524c,#cf3f3a)}
.nav ul{position:absolute;left:229px;top:0;display:flex;height:37px}
.nav li{font-family:"PT Sans",sans-serif;font-weight:700;font-size:13px;color:var(--white);line-height:37px;padding:0 20px}
.nav li.active{background:#ef8b86;font-weight:400;padding:0 9px;position:relative;margin-right:2px}
.nav li.active:before{content:"";position:absolute;left:50%;top:0;margin-left:-6px;border:6px solid transparent;border-top-color:var(--white)}

.slider{left:0;top:162px;width:1200px;height:341px;background:var(--slider)}
.slider .banner{left:331px;top:42px;width:539px;height:258px;background:radial-gradient(ellipse at 65% 45%,#1f5d86,#0b1b2a 60%,#050a10)}
.slider .arrow{top:112px;font-size:36px;font-weight:700;color:#111}

.section-title{left:229px;top:516px;font-family:"PT Sans",sans-serif;font-size:14px;color:#333}
.product{width:178px;text-align:center}
.product .frame{width:178px;height:120px;background:#e8e8e8;padding:4px}
.product .thumb{width:166px;height:112px;background:var(--white);border-left:1px solid #e7a29f;border-bottom:1px solid #e7a29f;display:flex;align-items:center;justify-content:center}
.product .icon{width:78px;height:78px;border-radius:50%}
.product .name{margin-top:16px;font-family:"PT Sans",sans-serif;font-size:12px;color:#777}
.product .price{margin-top:6px;font-family:"PT Sans",sans-serif;font-size:15px;color:#b0343a}

.rule{left:229px;top:922px;width:744px;height:1px;background:var(--line)}
.newsletter{left:229px;top:938px;display:flex;align-items:center;gap:9px}
.newsletter .label{font-family:"PT Sans",sans-serif;font-size:13px;color:#333}
.newsletter .field{width:118px;height:18px;background:var(--white);border:1px solid #ddd;font-size:9px;color:#aaa;padding:3px 8px;margin-left:2px}
.newsletter .btn{width:36px;height:18px;background:var(--red);color:var(--white);font-size:8px;font-weight:700;text-align:center;line-height:18px;margin-left:-9px}
.phone-block{left:862px;top:933px;display:flex;align-items:center;gap:10px;font-size:10px;color:#666;line-height:13px}

.footer{left:0;top:965px;width:1200px;height:189px;background:var(--dark)}
.col{top:16px}
.col h4{font-family:"PT Sans",sans-serif;font-size:12px;font-weight:400;color:var(--red-soft);margin-bottom:7px}
.col li{font-size:9.5px;color:var(--footer-text);height:19.2px;padding-left:12px;position:relative}
.col li:before{content:"";position:absolute;left:0;top:4px;width:4px;height:4px;border-radius:50%;background:var(--white)}
.follow{right:227px;top:16px;text-align:right;font-family:"PT Sans",sans-serif;font-size:12px;color:var(--white)}
.socials{display:flex;gap:6px;margin-top:12px;justify-content:flex-end}
.socials span{display:flex;align-items:center;gap:3px;font-family:Arial,sans-serif;font-size:9px;color:var(--footer-text)}
.socials i{width:10px;height:10px;border-radius:50%;background:#8fa6bd;display:block}
.payhead{margin-top:24px}
.pays{display:flex;gap:5px;margin-top:12px;justify-content:flex-end}
.pays span{width:38px;height:24px;background:var(--white);border-radius:2px;font-family:Arial,sans-serif;font-size:8px;color:#333;text-align:center;line-height:24px}
.to-top{left:1126px;top:1110px;width:38px;height:38px;border-radius:50%;background:var(--red)}

.bottombar{left:0;top:1154px;width:1200px;height:33px;background:var(--red);font-size:9.5px;color:var(--white)}
.bottombar .links{left:229px;top:11px;display:flex;gap:12px}
.bottombar .copy{right:227px;top:11px}
</style>
</head>
<body>

<div class="abs topbar">
  <div class="abs currency">Currency: <b>USD ▾</b></div>
  <div class="abs links"><span class="welcome">Default welcome msg!</span>My Account<span class="sep">|</span>My Wishlist<span class="sep">|</span>Checkout<span class="sep">|</span>Log In</div>
</div>

<div class="abs logo">LOGO</div>
<div class="abs tel">tel: (055) 27-41-306-12 (055) 273-461-306</div>
<div class="abs search"><div class="field">Search entire store here...</div><div class="btn">SEARCH</div></div>
<div class="abs cart">Shopping Cart - <b>$0.00</b>
  <svg width="13" height="11" viewBox="0 0 13 11"><path d="M0 1h2l2 6h7l2-5H3" fill="none" stroke="#777" stroke-width="1.3"/><circle cx="5" cy="9.5" r="1" fill="#777"/><circle cx="10" cy="9.5" r="1" fill="#777"/></svg>
</div>

<nav class="abs nav">
  <ul>
    <li class="active">Home</li>
    <li>Top 10</li>
    <li>Freeware</li>
    <li>Most Downloaded</li>
    <li>Mobile Applications</li>
  </ul>
</nav>

<div class="abs slider">
  <div class="abs arrow" style="left:28px">&lt;</div>
  <div class="abs banner" role="img" aria-label="Promotional banner: all-in-one desktop computer with keyboard on a dark blue background"></div>
  <div class="abs arrow" style="left:1148px">&gt;</div>
</div>

<div class="abs section-title">Featured Products</div>

<div class="abs product" style="left:235px;top:542px"><div class="frame"><div class="thumb"><div class="icon" role="img" aria-label="Green glossy software icon" style="background:radial-gradient(#7fe05a,#1d7a22 70%,#333)"></div></div></div><div class="name">Modern Wicker Garden</div><div class="price">$100.00</div></div>
<div class="abs product" style="left:420px;top:542px"><div class="frame"><div class="thumb"><div class="icon" role="img" aria-label="Orange and blue browser-style software icon" style="background:radial-gradient(circle at 40% 40%,#4c7fd0,#e0641e 60%,#b33a10)"></div></div></div><div class="name">Rattan furniture in conservatory</div><div class="price">$100.00</div></div>
<div class="abs product" style="left:606px;top:542px"><div class="frame"><div class="thumb"><div class="icon" role="img" aria-label="Bronze glossy software icon" style="background:radial-gradient(#e9b04a,#7a5a2a 65%,#2a2a2a)"></div></div></div><div class="name">Modern Outside Patio Furniture</div><div class="price">$100.00</div></div>
<div class="abs product" style="left:794px;top:542px"><div class="frame"><div class="thumb"><div class="icon" role="img" aria-label="Teal glossy software icon" style="background:radial-gradient(#7fd8ea,#1a7f98 65%,#2a2a2a)"></div></div></div><div class="name">3d Furnitures</div><div class="price">$100.00</div></div>

<div class="abs product" style="left:235px;top:723px"><div class="frame"><div class="thumb"><div class="icon" role="img" aria-label="Red and black software icon" style="border-radius:6px;background:linear-gradient(135deg,#e24040,#7a1010 60%,#333)"></div></div></div><div class="name">Wrought Iron Furniture</div><div class="price">$100.00</div></div>
<div class="abs product" style="left:420px;top:723px"><div class="frame"><div class="thumb"><div class="icon" role="img" aria-label="Blue and green music software icon" style="background:radial-gradient(#5ed0c0,#2a5aa8 60%,#222)"></div></div></div><div class="name">New and beautiful furniture</div><div class="price">$100.00</div></div>
<div class="abs product" style="left:606px;top:723px"><div class="frame"><div class="thumb"><div class="icon" role="img" aria-label="Colourful character software icon" style="background:radial-gradient(#9be05a,#2f9a3a 55%,#f2f2f2 72%)"></div></div></div><div class="name">Furniture plastic wheel</div><div class="price">$100.00</div></div>
<div class="abs product" style="left:794px;top:723px"><div class="frame"><div class="thumb"><div class="icon" role="img" aria-label="Silver and red flame software icon" style="background:radial-gradient(#f08040,#b02818 50%,#777 75%)"></div></div></div><div class="name">Texture of rattan furniture</div><div class="price">$100.00</div></div>

<div class="abs rule"></div>
<div class="abs newsletter">
  <svg width="30" height="20" viewBox="0 0 30 20"><rect x="1" y="1" width="28" height="18" fill="#888"/><path d="M1 1l14 10L29 1M1 19l10-9M29 19l-10-9" fill="none" stroke="#ededed" stroke-width="1.6"/></svg>
  <span class="label">Sign up for Newsletter</span>
  <span class="field">Enter your email address</span>
  <span class="btn">SUBMIT</span>
</div>
<div class="abs phone-block">
  <svg width="26" height="24" viewBox="0 0 26 24"><path d="M2 8c0-5 22-5 22 0v3h-6V8H8v3H2z" fill="#777"/><path d="M6 11h14l3 11H3z" fill="#888"/><circle cx="13" cy="16" r="3" fill="#ededed"/></svg>
  <div>(055) 27-41-306<br>(055) 27-41-306</div>
</div>

<footer class="abs footer">
  <div class="abs col" style="left:229px"><h4>OUR OFFERS</h4><ul><li>New products</li><li>Top sellers</li><li>Specials</li><li>Manufacturers</li><li>Suppliers</li><li>Specials</li><li>Service</li></ul></div>
  <div class="abs col" style="left:336px"><h4>SHIPPING INFO</h4><ul><li>Returns</li><li>Delivery</li><li>Service</li><li>Gift Cards</li><li>Mobile</li><li>Gift Cards</li><li>Manufacturers</li></ul></div>
  <div class="abs col" style="left:450px"><h4>OUR ACCOUNT</h4><ul><li>Your Account</li><li>information</li><li>Addresses</li><li>Discount</li><li>Orders history</li><li>Addresses</li><li>Search Terms</li></ul></div>
  <div class="abs col" style="left:564px"><h4>OUR SUPPORT</h4><ul><li>Site Map</li><li>Search Terms</li><li>Advanced Search</li><li>Mobile</li><li>Contact Us</li><li>Mobile</li><li>Addresses</li></ul></div>
  <div class="abs follow">
    <div>FLLOW US</div>
    <div class="socials"><span><i></i>Chatly</span><span><i></i>Tweeko</span><span><i></i>Vidzo</span><span><i></i>Feedr</span></div>
    <div class="payhead">CONNECT PAYMENT</div>
    <div class="pays"><span>Paylo</span><span>Dizcard</span><span>Varda</span><span>Amberex</span><span>Mastora</span></div>
  </div>
</footer>

<div class="abs to-top">
  <svg width="38" height="38" viewBox="0 0 38 38"><path d="M12 22l7-7 7 7" fill="none" stroke="#fff" stroke-width="2.4"/></svg>
</div>

<div class="abs bottombar">
  <div class="abs links"><span>Site Map</span><span>Search Terms</span><span>Advanced Search</span><span>Orders and Returns</span><span>Contact Us</span></div>
  <div class="abs copy">© 2013 . All Rights Reserved.</div>
</div>

</body>
</html>
```